Australian new start up company needs a Logo & Web Design

We need a smart, simple logo and web design for a new start up company based in Melbourne Australia called "Tidewater Enterprise Assist". The logo is to be used on all marketing materials. The website is the primary interface of the company.

Our initial phase (launch) will provide a B2B directory service, resources and solutions.
A.) By listing on our site, small businesses can generate sales for their business. Regardless of where they might be located in the world, then can sell to Australian small businesses.
B.)Through our resource centre, small businesses can find practical and up to date resources for their business in pre-start up, start up, growth, maintenance and succession planning or exit stage.
C.)And on our site, we'll offer time and money saving solutions. These solutions can be packaged solutions (ie. Car Branding = including design, print and application onto the vehicle at a discounted price). Customers can also contact us if they want to advertise their business solution.

Eventually, there will be a total of five services inclusive of the directory described above (ie. business classifieds, link to Asian businesses, expos/seminars listing, etc). We hope to see this site grow over the next 18 months. All services will be aimed at servicing small businesses. Individuals through to large businesses located any where in the world can service these small businesses.

We would like to see designs that are professional. They should communicate growth, trust, professionalism and forward thinking.

Target Market(s)

Small Businesses (ie. employ up to 150 employees)

Industry/Entity Type

Business

Requirements
Must have
• We have attached some of the current files that we have designed ourselves. We feel that our material is lacking in appeal, professionalism and consistency. However, it does give a good idea of the requirements needed such as login, directory on the frontpage, etc. The wording is not final, as we are trying to finalise the design first. The logo was simply a placeholder as that definitely needs to be designed.

We want a logo and website that sticks in people's minds, its memorable.

We want a website that is EASY to use and navigate.
Nice to have
• Eventually, there will be a total of five services inclusive of the directory described above (ie. business classifieds, Asian businesses, expos/seminars listing, etc). They are very different types of services. The common thread is that all services will be aimed at servicing small businesses.

The winning design will need to help us to visualize how their design suits our future growth.

```html
<!DOCTYPE html>
<html lang="en">
<head>
<meta charset="utf-8">
<title>Tidewater Enterprise Assist</title>
<link href="https://fonts.googleapis.com/css2?family=Roboto+Condensed:wght@300;400;700&display=swap" rel="stylesheet">
<style>
:root{
  --paper:#f7f7f7;
  --ink:#222;
  --ink-soft:#555;
  --ink-faint:#888;
  --band:#2b2b2b;
  --band-dark:#1e1e1e;
  --field:#f2f2f2;
  --card:#cfcfcf;
  --white:#fff;
  --violet:#8a2a9a;
  --navy:#1e3c6e;
  --crimson:#a41e1e;
  --amber:#d86a12;
}
*{box-sizing:border-box;margin:0;padding:0}
html,body{width:1200px;height:1200px;overflow:hidden}
body{position:relative;background:var(--paper);font-family:"Roboto Condensed",Arial,sans-serif;color:var(--ink)}
.abs{position:absolute}

/* header */
.brand-mark{left:186px;top:88px;width:58px;height:58px;border-radius:50%;background:var(--ink)}
.brand-name{left:186px;top:170px;font-size:36px;font-weight:300;letter-spacing:.5px;color:var(--ink);white-space:nowrap}
.tagline{left:185px;top:216px;font-size:17px;font-weight:400;letter-spacing:.3px}
.perks{right:540px;top:251px;text-align:right;font-size:12.5px;line-height:15.6px;color:var(--ink-soft);font-weight:300}
.login{left:784px;top:219px;width:145px}
.login .input{height:23px;border:2px solid #9a9a9a;border-radius:7px;background:var(--white);font-size:11px;color:#999;padding:2px 6px;margin-bottom:9px;box-shadow:inset 0 1px 2px rgba(0,0,0,.15)}
.login .buttons{display:flex;gap:4px;margin-top:1px}
.btn{height:22px;border-radius:7px;background:var(--band);color:var(--white);font-weight:700;display:flex;align-items:center;justify-content:center}
.btn.post{width:52px;font-size:9px}
.btn.go{flex:1;font-size:12px}
.forgot{font-size:9px;color:var(--ink-soft);text-align:right;margin-top:7px}

/* search band */
.search-band{left:0;top:328px;width:1200px;height:140px;background:linear-gradient(180deg,var(--band-dark),var(--band) 50%,var(--band-dark))}
.search-label{color:var(--white);font-size:21px;font-weight:400;top:386px}
.search-field{top:388px;height:22px;border-radius:8px;background:var(--field);box-shadow:inset 0 2px 3px rgba(0,0,0,.35)}

/* categories */
.cat-title{left:189px;top:503px;font-size:15.5px;font-weight:400;letter-spacing:.4px}
.cat-list{list-style:none;font-size:12.5px;color:var(--ink-soft);font-weight:300;letter-spacing:.2px}
.cat-list li{position:relative;padding-left:20px;height:20.1px;line-height:20px}
.cat-list li::before,.cat-list li::after{content:"";position:absolute;background:var(--ink)}
.cat-list li::before{left:0;top:9px;width:13px;height:3px}
.cat-list li::after{left:5px;top:4px;width:3px;height:13px}
.cat-list li.sub{padding-left:32px;height:12.6px;line-height:12.6px;font-size:10px;color:var(--ink-faint)}
.cat-list li.sub::before,.cat-list li.sub::after{display:none}
.resource-link{left:771px;top:820px;font-size:16px;letter-spacing:.4px;display:flex;align-items:center;gap:10px}

/* packages */
.deal-band{left:0;top:855px;width:1200px;height:325px;background:var(--band)}
.card{top:880px;width:160px;height:120px;border-radius:6px;background:var(--card);overflow:hidden;box-shadow:0 2px 4px rgba(0,0,0,.5)}
.card-corner{position:absolute;right:0;bottom:0;width:62px;height:70px;background:var(--band-dark);clip-path:polygon(100% 0,100% 100%,0 100%)}
.card-go{position:absolute;right:9px;bottom:6px;color:var(--white);font-size:18px;font-weight:700}
.card-title{position:absolute;left:0;right:0;top:8px;text-align:center;color:var(--white);font-size:16.5px;font-weight:700;letter-spacing:.4px;text-shadow:0 1px 2px rgba(0,0,0,.6)}
.card-price{position:absolute;left:14px;top:29px;font-size:18px;font-weight:700;text-shadow:0 1px 1px rgba(0,0,0,.4)}
.card-body{position:absolute;left:14px;top:55px;font-size:12px;line-height:13px;color:var(--ink)}

/* footer */
.social{left:761px;top:1086px;display:flex;gap:24px}
.social span{width:18px;height:18px;background:#e4e4e4;border-radius:2px}
.foot-nav{top:1128px;font-size:10.5px;color:var(--white);font-weight:400}
.legal{left:0;width:1103px;top:1155px;text-align:center;font-size:8.5px;color:#ddd}
.foot-strip{left:0;top:1180px;width:1200px;height:20px;background:var(--paper)}
</style>
</head>
<body>

<header>
  <div class="abs brand-mark"></div>
  <div class="abs brand-name">TIDEWATER ENTERPRISE ASSIST</div>
  <p class="abs tagline">Online directory, dedicated to servicing Australian Small Businesses</p>
  <p class="abs perks">Advertise for as little as $2/month<br>Generate sales, increase brand awareness<br>Limited time business offers<br>Small Business resource centre</p>
  <form class="abs login">
    <div class="input">Username</div>
    <div class="input">Password</div>
    <div class="buttons"><div class="btn post">Post an Ad</div><div class="btn go">Login</div></div>
    <p class="forgot">Forgotten your login details?</p>
  </form>
</header>

<section>
  <div class="abs search-band"></div>
  <span class="abs search-label" style="left:194px">I need</span>
  <div class="abs search-field" style="left:282px;width:237px"></div>
  <span class="abs search-label" style="left:670px">located in</span>
  <div class="abs search-field" style="left:786px;width:142px"></div>
</section>

<section>
  <h2 class="abs cat-title">Browse by Categories</h2>
  <ul class="abs cat-list" style="left:188px;top:545px">
    <li>Accounting</li>
    <li>Artwork Design</li>
    <li class="sub">Banner</li><li class="sub">Blog</li><li class="sub">Brochure</li>
    <li class="sub">Electronic Stationary</li><li class="sub">Templates</li><li class="sub">Social Media</li>
    <li class="sub">Flyers</li><li class="sub">Logos</li>
    <li>Banking and Finance</li><li>Bookkeeping</li><li>Category</li><li>Category</li><li>Category</li><li>Category</li>
  </ul>
  <ul class="abs cat-list" style="left:449px;top:545px">
    <li>Capital Raising</li><li>Cleaning Services</li><li>Coaching and Training</li><li>Courier Service</li>
    <li>Equipment Hire</li><li>Event Planning/Coordination</li><li>Facilities</li><li>Fitness and Health</li>
    <li>Information Technology</li><li>Insurance</li><li>Legal Advice</li><li>Panufacturing</li>
    <li>Marketing and Public Relations</li>
  </ul>
  <ul class="abs cat-list" style="left:751px;top:545px">
    <li>Photography/Videography</li><li>Printing</li><li>Promotional Materials</li><li>recruitment</li>
    <li>Sales</li><li>Sewing and Tailoring</li><li>Signage and Stationary</li><li>Superannuation</li>
    <li>Tradesman</li><li>travel Services</li><li>Uniforms/Corporate Wear</li><li>repair and Maintenance</li>
    <li>Virtual Assistants</li>
  </ul>
  <div class="abs resource-link">View Resource Centre
    <svg width="14" height="24" viewBox="0 0 14 24"><path d="M2 2 L12 12 L2 22" fill="none" stroke="#222" stroke-width="2.5"/></svg>
  </div>
</section>

<section>
  <div class="abs deal-band"></div>
  <div class="abs card" style="left:180px"><div class="card-corner"></div><div class="card-title">Start-Up Package</div><div class="card-price" style="color:var(--violet)">$2000</div><div class="card-body">Logo Design<br>Website Design<br>Stationary<br>Directory Listing</div><div class="card-go">Go</div></div>
  <div class="abs card" style="left:381px"><div class="card-corner"></div><div class="card-title">Biz Growth Package</div><div class="card-price" style="color:var(--navy)">$1000</div><div class="card-body">Logo Design<br>Website Design<br>Stationary<br>Directory Listing</div><div class="card-go">Go</div></div>
  <div class="abs card" style="left:580px"><div class="card-corner"></div><div class="card-title">Business Coaching</div><div class="card-price" style="color:var(--crimson)">$2500</div><div class="card-body">XX hours of business<br>coaching;<br>Directory Listing.</div><div class="card-go">Go</div></div>
  <div class="abs card" style="left:781px"><div class="card-corner"></div><div class="card-title">Vehicle Advertising</div><div class="card-price" style="color:var(--amber)">$1200</div><div class="card-body">Artwork Printing<br>Vehicle Placement<br>Directory Listing</div><div class="card-go">Go</div></div>
</section>

<footer>
  <div class="abs social"><span></span><span></span><span></span><span></span></div>
  <span class="abs foot-nav" style="left:217px">How it Works</span>
  <span class="abs foot-nav" style="left:307px">Login</span>
  <span class="abs foot-nav" style="left:375px">Resource Centre</span>
  <span class="abs foot-nav" style="left:487px">Terms and Conditions</span>
  <span class="abs foot-nav" style="left:622px">Post an ad</span>
  <span class="abs foot-nav" style="left:712px">Contact Us</span>
  <span class="abs foot-nav" style="left:802px">Asia Link</span>
  <span class="abs foot-nav" style="left:870px">Privacy</span>
  <p class="abs legal">©Tidewater Enterprise Assist Group 2012. Use of this website constitutes acceptance of our Terms and Conditions and Privacy Policy</p>
  <div class="abs foot-strip"></div>
</footer>

</body>
</html>
```